Hero Image Redesign for VELM Consulting Website

About us:
VELM Consulting is an organisational psychology and human resource management consulting firm based in Melbourne, Australia (www.velmadvisory-example.com.au). We are a B2B offering a range of organisational psychology measurement and consulting. The largest part of our business is our online psychometric assessments, which are self-managed via an online portal, which is currently used by many organisations worldwide as part of their recruitment process.

What we are looking for:
We are seeking assistance to redesign an image located above the fold - on the top right hand side of homepage. We want an image of a small group of diverse people happily working together using a laptop (either individually or as a group), overlayed with graphic representations reflective of using our online Psychometric Assessment tool, in an interactive fashion.

The graphics will highlight key features of the self-service VELM Psychometric Assessment Portal, specifically ease of use, flexibility and our integrated approach. We want the image to look clean, clear, minimal, with use of negative space. All graphics must be accessible (including sufficient colour contrast and text size).

We would like the graphic to feature 3 “pop ups” highlighting features, and these should appear over the image:

1. Setup participants easily online
2. Check the status of an assessment
3. View participants’ reports

Examples from other SaaS websites attached.

The final design should communicate trust, reliability, our scientific evidence based approach, and our approachable and friendly customer service.

Our main brand colours are:
• Navy – HEX #2F2971
• Mid Blue – HEX #0C75C0
• Black – HEX #000000

About VELM’ website and potential for future work:

• VELM’ website pages have been created using Bricks Builder for WordPress.
• There is a strong possibility of future projects following successful delivery. We are an excellent client – ethical, professional and with a genuine commitment to partnership.

Need extra days to review

```html
<!DOCTYPE html>
<html lang="en">
<head>
<meta charset="utf-8">
<title>VELM Consulting – Organisational Psychology Consulting</title>
<link rel="stylesheet" href="https://fonts.googleapis.com/css2?family=Plus+Jakarta+Sans:wght@400;500;600;700&family=Poppins:wght@400;500;600&display=swap">
<style>
  :root {
    --navy: #2f2971;
    --navy-deep: #2b2568;
    --teal: #a8e2dc;
    --teal-line: #9fdcd5;
    --nav-bg: #f6f6f6;
    --ink: #222222;
    --body-grey: #4a4a4a;
    --white: #ffffff;
  }
  * { box-sizing: border-box; margin: 0; padding: 0; }
  html, body {
    width: 1200px; height: 675px; overflow: hidden;
    background: var(--white);
    font-family: "Plus Jakarta Sans", sans-serif;
  }
  .page { position: relative; width: 1200px; height: 675px; overflow: hidden; }

  .announce {
    height: 40px; background: var(--navy); color: var(--white);
    display: flex; align-items: center; justify-content: center;
    font-size: 12.5px; font-weight: 600; gap: 6px;
  }
  .announce a { color: var(--teal); text-decoration: underline; font-weight: 500; }

  .site-header {
    height: 64px; background: var(--nav-bg);
    display: flex; align-items: center; justify-content: space-between;
    padding: 0 50px 0 37px;
  }
  .brand { display: flex; align-items: center; gap: 8px; color: var(--navy);
    font-weight: 700; font-size: 22px; letter-spacing: -0.2px; }
  .brand-mark { width: 18px; height: 18px; border-radius: 50%; background: var(--teal); }
  .main-nav { display: flex; gap: 26px; font-size: 13px; color: var(--ink); font-weight: 500; }
  .main-nav span { display: flex; align-items: center; gap: 7px; }
  .main-nav svg { width: 10px; height: 7px; }

  .hero-copy { position: absolute; left: 67px; top: 166px; width: 520px; }
  .hero-title { color: var(--navy); font-size: 61px; font-weight: 600; line-height: 68px; letter-spacing: -0.3px; }
  .hero-lead { margin-top: 28px; color: var(--body-grey); font-size: 20.5px; line-height: 38px; width: 520px; }
  .hero-actions { position: absolute; top: 530px; left: 67px; display: flex; gap: 35px; }
  .btn { height: 52px; border-radius: 3px; display: flex; align-items: center; justify-content: center;
    font-size: 14.5px; font-weight: 700; box-shadow: 0 3px 6px rgba(0,0,0,0.12); }
  .btn-primary { width: 198px; background: var(--navy); color: var(--white); }
  .btn-secondary { width: 199px; background: var(--teal); color: var(--navy); gap: 8px; }

  .hero-visual { position: absolute; left: 0; top: 0; }
  .team-photo {
    position: absolute; left: 712px; top: 193px; width: 347px; height: 359px; border-radius: 18px;
    background: linear-gradient(160deg, #b9a890 0%, #8d8a7a 30%, #c9d2d6 60%, #5e6b78 100%);
  }
  .popup {
    position: absolute; width: 184px; height: 82px; background: var(--white); border-radius: 6px;
    font-family: "Poppins", sans-serif; font-size: 16.5px; line-height: 20px; color: #111;
    display: flex; align-items: center; padding: 0 18px;
  }
  .popup-status { left: 575px; top: 254px; border: 2px solid var(--teal-line); }
  .popup-setup { left: 964px; top: 209px; border: 2px solid var(--navy); }
  .popup-reports {
    position: absolute; left: 810px; top: 517px; width: 186px; height: 65px; border-radius: 3px;
    background: var(--navy); color: var(--white); font-family: "Poppins", sans-serif;
    font-weight: 600; font-size: 16.5px; line-height: 20px; text-align: center;
    display: flex; align-items: center; justify-content: center; outline: 4px solid var(--white);
  }
  .badge { position: absolute; border-radius: 50%; display: flex; align-items: center; justify-content: center; }
  .badge-status { left: 615px; top: 346px; width: 52px; height: 52px; background: var(--teal); }
  .badge-setup { left: 1078px; top: 154px; width: 50px; height: 50px; background: var(--navy); }
</style>
</head>
<body>
<div class="page">
  <div class="announce">
    <span>Register now for our <a>free virtual workshops</a></span>
    <span>|</span>
    <span>VELM Consulting Clients: <a>Login to the Portal</a></span>
  </div>

  <header class="site-header">
    <div class="brand"><span class="brand-mark"></span>VELM Consulting</div>
    <nav class="main-nav">
      <span>Psychometric testing <svg viewBox="0 0 10 7"><path d="M1 1l4 4 4-4" fill="none" stroke="#222" stroke-width="1.6"/></svg></span>
      <span>Employee wellbeing <svg viewBox="0 0 10 7"><path d="M1 1l4 4 4-4" fill="none" stroke="#222" stroke-width="1.6"/></svg></span>
      <span>HR consulting <svg viewBox="0 0 10 7"><path d="M1 1l4 4 4-4" fill="none" stroke="#222" stroke-width="1.6"/></svg></span>
      <span>Events</span>
      <span>Knowledge hub <svg viewBox="0 0 10 7"><path d="M1 1l4 4 4-4" fill="none" stroke="#222" stroke-width="1.6"/></svg></span>
      <span>About us <svg viewBox="0 0 10 7"><path d="M1 1l4 4 4-4" fill="none" stroke="#222" stroke-width="1.6"/></svg></span>
      <span>Contact</span>
    </nav>
  </header>

  <section class="hero-copy">
    <h1 class="hero-title">Organisational<br>Psychology<br>Consulting</h1>
    <p class="hero-lead">Optimise your workforce with psychometric testing, engagement surveys, wellbeing measures, and organisational development.</p>
  </section>

  <div class="hero-actions">
    <a class="btn btn-primary">Psychometric Testing</a>
    <a class="btn btn-secondary">Speak to an Expert
      <svg width="11" height="10" viewBox="0 0 11 10"><path d="M0 5h9M6 1.5L9.5 5 6 8.5" fill="none" stroke="#2f2971" stroke-width="1.5"/></svg>
    </a>
  </div>

  <div class="hero-visual">
    <div class="team-photo" role="img" aria-label="Three colleagues smiling while working together on a laptop in a bright office"></div>

    <div class="popup popup-status">Check the Status of an Assessment</div>
    <div class="badge badge-status">
      <svg width="28" height="28" viewBox="0 0 28 28" fill="none" stroke="#2f2971" stroke-width="1.6">
        <rect x="5" y="4" width="16" height="21" rx="1.5"/>
        <rect x="10" y="2" width="6" height="4" rx="1"/>
        <path d="M8 11l1.5 1.5L12 10M8 17l1.5 1.5L12 16M14 11.5h4M14 17.5h3"/>
        <path d="M19 22l6-8 1.8 1.4-6 8-2.3.8z"/>
      </svg>
    </div>

    <div class="popup popup-setup">Setup Participants Easily Online</div>
    <div class="badge badge-setup">
      <svg width="30" height="30" viewBox="0 0 30 30" fill="none" stroke="#ffffff" stroke-width="1.3">
        <circle cx="15" cy="15" r="11"/>
        <circle cx="15" cy="12" r="2.3"/>
        <path d="M11 19c0-2.4 1.8-4 4-4s4 1.6 4 4"/>
        <circle cx="15" cy="4" r="1.6" fill="#ffffff"/>
        <circle cx="4" cy="15" r="1.6" fill="#ffffff"/>
        <circle cx="26" cy="15" r="1.6" fill="#ffffff"/>
        <circle cx="15" cy="26" r="1.6" fill="#ffffff"/>
      </svg>
    </div>

    <div class="popup-reports">View participants’<br>reports</div>
  </div>
</div>
</body>
</html>
```